jewellery store flyer

Front to show
-company name and logo
underneath of company name, I want " The perfect creation" to be written.
-background bright tone jewellery or model wearing jewellery(prefer engagement and wedder or wedder set)

--------------------------------------------------------------
Back to show list of service and brief map of location
with addresss and contact detail

introducing newly established jewellery store with exclusive and unique jewellery. We offer you
-specialized in hand made jewellery
-on site jeweller and designer
-repair and restoring
-laser engraving and laser solder

4/31 Tarrawin Crescent Griffith ACT 2603
02) 6148 3072
Enquiry: marlow.k@postvane.com
---------------------------------------------------------------------
I have enclosed mockups that I made by myself, to show what I was thinking. this is just for reference. New flyer doesn't need to look the same.

I don't mind either holizontal nor vertical.
I don't mind if you add text or remove text that I have written above.
I want flyer to look morden and neat.

Good luck to you & me and enjoy creation.
Kind regards,
Pearl

Target Market(s)

introducing newly established store.
aiming for engagement & wedding rings and remakes

Industry/Entity Type

It Company

Font styles to use
Other font styles liked:
• Monotype corsive for script but name and address for SERIF

Colors

Designer to choose colors to be used in the design.

Requirements
Must have
• background photo including jewellery
• company name and address
• service detail
Nice to have
• brief map of location( I have red circled few places that people know more on the map I attached here.)
• Map to be simplified please.
• Please do not use Google map directly.
• Opening hours: Mon-Fri 9.30 to 5.30 Sat 10.00 to 5

```html
<!DOCTYPE html>
<html lang="en">
<head>
<meta charset="utf-8">
<title>Ardent Jewellery – Flyer</title>
<link rel="stylesheet" href="https://fonts.googleapis.com/css2?family=Cormorant+Garamond:wght@400;500;600&display=swap">
<style>
  :root {
    --canvas: #e4e4e5;
    --ink: #141414;
    --panel: rgba(52, 46, 44, 0.9);
    --band: rgba(78, 72, 70, 0.82);
    --paper: #f4f2ef;
    --muted: #cfc9c4;
    --badge: #d9d9d9;
    --ray-1: #3a3a3a;
    --ray-2: #555;
    --ray-3: #777;
    --ray-4: #9a9a9a;
  }
  * { box-sizing: border-box; margin: 0; padding: 0; }
  html, body { width: 1200px; height: 1000px; overflow: hidden; }
  body {
    background: var(--canvas);
    font-family: "Cormorant Garamond", Georgia, serif;
    color: var(--paper);
    position: relative;
  }
  .flyer {
    position: absolute;
    overflow: hidden;
    background: var(--ink);
    box-shadow: 0 10px 24px rgba(0,0,0,0.25);
  }

  /* Front */
  .flyer--front { left: 280px; top: 30px; width: 640px; height: 430px; }
  .front-photo {
    position: absolute; inset: 0;
    background:
      radial-gradient(ellipse at 45% 45%, #d9b8a8 0%, #c39a88 30%, transparent 60%),
      linear-gradient(180deg, #c8a898 0%, #8d95b0 60%, #6f7ea8 100%);
  }
  .front-shapes { position: absolute; inset: 0; }
  .brand-mark {
    position: absolute; left: 22px; top: 22px;
    display: flex; align-items: center; gap: 8px;
    font-size: 22px; font-weight: 500; color: var(--paper);
  }
  .brand-mark .dot { width: 10px; height: 10px; border-radius: 50%; background: var(--paper); }
  .title-band {
    position: absolute; left: 0; right: 0; top: 200px; height: 100px;
    background: var(--band);
    display: flex; align-items: center; gap: 40px;
    padding: 0 30px 0 60px;
  }
  .company-name {
    font-size: 40px; font-weight: 500; line-height: 0.95;
    letter-spacing: 1px; text-transform: uppercase;
    white-space: nowrap; flex: none;
  }
  .tagline {
    font-size: 32px; font-weight: 400; white-space: nowrap;
    align-self: flex-end; padding-bottom: 14px; flex: none;
  }

  /* Backs */
  .flyer--back { top: 520px; width: 540px; height: 450px; }
  .flyer--contact { left: 40px; }
  .flyer--services { left: 620px; }
  .back-photo {
    position: absolute; left: 0; right: 0; top: 0; height: 210px;
  }
  .flyer--contact .back-photo {
    background: linear-gradient(120deg, #d49a72 0%, #b27755 45%, #6a4a3c 100%);
  }
  .flyer--services .back-photo {
    background: linear-gradient(100deg, #2a2222 0%, #3b2e2c 40%, #c49a86 75%, #dcb4a2 100%);
  }
  .back-panel {
    position: absolute; left: 0; right: 0; top: 210px; bottom: 0;
    background: var(--panel);
    padding: 62px 40px 16px;
  }
  .badge {
    position: absolute; top: 165px; width: 90px; height: 90px;
    border-radius: 50%; background: var(--badge);
    border: 4px solid #2d2a29;
    z-index: 1;
  }
  .flyer--contact .badge { left: 225px; }
  .flyer--services .badge--one { left: 155px; }
  .flyer--services .badge--two { left: 295px; }
  .contact-list { list-style: none; font-size: 22px; line-height: 1.35; color: var(--muted); padding-top: 20px; }
  .intro { font-size: 18px; line-height: 1.2; }
  .service-list { list-style: none; font-size: 18px; line-height: 1.2; margin-top: 4px; }
  .service-list li::before { content: "-"; }
</style>
</head>
<body>

<section class="flyer flyer--front">
  <div class="front-photo" role="img" aria-label="Photograph of a model in profile wearing a black beaded necklace, hand raised to the chin"></div>
  <svg class="front-shapes" width="640" height="430" viewBox="0 0 640 430" aria-hidden="true">
    <polygon points="0,0 170,0 110,130 0,130" fill="var(--ink)"/>
    <polygon points="110,130 170,0 150,200 80,200" fill="var(--ray-4)" opacity="0.55"/>
    <polygon points="540,300 640,300 640,430 600,430" fill="var(--ink)"/>
    <polygon points="540,300 600,430 575,430" fill="var(--ray-1)"/>
    <polygon points="540,300 575,430 555,430" fill="var(--ray-2)"/>
    <polygon points="540,300 555,430 540,430" fill="var(--ray-3)"/>
    <polygon points="540,300 540,430 528,430" fill="var(--ray-4)"/>
  </svg>
  <div class="brand-mark"><span class="dot"></span>Ardent</div>
  <div class="title-band">
    <h1 class="company-name">Ardent<br>Jewellery</h1>
    <p class="tagline">The Perfect Creation</p>
  </div>
</section>

<section class="flyer flyer--back flyer--contact">
  <div class="back-photo" role="img" aria-label="Photograph of a model wearing a sparkling diamond necklace"></div>
  <div class="badge" aria-hidden="true"></div>
  <div class="back-panel">
    <ul class="contact-list">
      <li>4/31 Tarrawin Crescent</li>
      <li>Griffith ACT 2603</li>
      <li>T: 02) 6148 3072</li>
      <li>Enquiry: marlow.k@postvane.com</li>
    </ul>
  </div>
</section>

<section class="flyer flyer--back flyer--services">
  <div class="back-photo" role="img" aria-label="Photograph of a model with dark hair wearing a statement earring"></div>
  <div class="badge badge--one" aria-hidden="true"></div>
  <div class="badge badge--two" aria-hidden="true"></div>
  <div class="back-panel">
    <p class="intro">Introducing newly established jewellery store with exclusive and unique jewellery.<br>We offer you:</p>
    <ul class="service-list">
      <li>Repair and restoring</li>
      <li>On site jeweller and designer</li>
      <li>Laser engraving and laser solder</li>
      <li>Specialized in hand made jewellery</li>
    </ul>
  </div>
</section>

</body>
</html>
```